Plumbing Business needs a more appealing business card design and logo

card must include phone number and logo, open to new logo ideas, full creative freedom

Industry/Entity Type

Plumbing

Contact Information for Business Card

Derek Halloway
0417385521

Logo Text

call outs from $80

Font styles to use
Other font styles liked:
• unsure

Colors
ec1f27
0255a3
f78f20

```html
<!DOCTYPE html>
<html lang="en">
<head>
<meta charset="utf-8">
<title>Keystone Plumbing – Business Card</title>
<link href="https://fonts.googleapis.com/css2?family=Montserrat:wght@700&family=Open+Sans:wght@400&display=swap" rel="stylesheet">
<style>
  :root {
    --backdrop: #d9d8d5;
    --card-white: #ffffff;
    --card-dark: #2f2f31;
    --brand-blue: #1a73c6;
    --ink: #111111;
    --muted: #444444;
    --emboss: #3a3a3d;
  }
  * { margin: 0; padding: 0; box-sizing: border-box; }
  html, body {
    width: 1200px; height: 801px; overflow: hidden;
    background: var(--backdrop);
  }
  .stage {
    position: relative; width: 1200px; height: 801px;
    display: flex; align-items: center; justify-content: center; gap: 40px;
  }
  .card {
    width: 525px; height: 300px; position: relative;
    box-shadow: 0 6px 18px rgba(0,0,0,0.18);
  }
  .card--front { background: var(--card-white); }
  .card--back { background: var(--card-dark); display: flex; align-items: center; justify-content: center; }

  .brand {
    position: absolute; top: 62px; left: 0; right: 0;
    display: flex; align-items: center; justify-content: center; gap: 12px;
  }
  .brand__dot {
    width: 22px; height: 22px; border-radius: 50%; background: var(--brand-blue);
  }
  .brand__name {
    font-family: "Montserrat", sans-serif; font-weight: 700;
    font-size: 30px; letter-spacing: 1px; text-transform: uppercase;
    color: var(--ink);
  }

  .contact-row {
    position: absolute; left: 50px; right: 30px; bottom: 60px;
    display: flex; align-items: center; gap: 24px;
  }
  .person__name {
    font-family: "Montserrat", sans-serif; font-weight: 700;
    font-size: 24px; color: var(--brand-blue); text-transform: uppercase;
    letter-spacing: 0.5px; line-height: 1;
  }
  .person__role {
    font-family: "Open Sans", sans-serif; font-size: 14px; color: var(--ink);
    text-align: right; margin-top: 2px;
  }
  .divider { width: 1.5px; height: 52px; background: var(--brand-blue); }
  .details { list-style: none; font-family: "Open Sans", sans-serif; font-size: 14px; color: var(--muted); }
  .details li { display: flex; align-items: center; gap: 6px; line-height: 1.6; }
  .details svg { width: 12px; height: 12px; fill: var(--brand-blue); flex: none; }

  .back-mark {
    font-family: "Montserrat", sans-serif; font-weight: 700;
    font-size: 40px; letter-spacing: 2px; text-transform: uppercase;
    color: var(--emboss);
  }
</style>
</head>
<body>
<main class="stage">
  <section class="card card--front" aria-label="Business card front">
    <div class="brand">
      <span class="brand__dot"></span>
      <span class="brand__name">Keystone Plumbing</span>
    </div>
    <div class="contact-row">
      <div class="person">
        <p class="person__name">Derek Halloway</p>
        <p class="person__role">owner</p>
      </div>
      <span class="divider"></span>
      <ul class="details">
        <li>
          <svg viewBox="0 0 24 24" aria-hidden="true"><path d="M6.6 10.8a15.1 15.1 0 0 0 6.6 6.6l2.2-2.2a1 1 0 0 1 1-.25 11.4 11.4 0 0 0 3.6.57 1 1 0 0 1 1 1V20a1 1 0 0 1-1 1A17 17 0 0 1 3 4a1 1 0 0 1 1-1h3.5a1 1 0 0 1 1 1c0 1.25.2 2.45.57 3.57a1 1 0 0 1-.25 1z"/></svg>
          0417 385 521
        </li>
        <li>
          <svg viewBox="0 0 24 24" aria-hidden="true"><path d="M2 5h20v14H2z M2 5l10 8 10-8" /></svg>
          derek@keystone-plumbing.com
        </li>
      </ul>
    </div>
  </section>

  <section class="card card--back" aria-label="Business card back">
    <span class="back-mark">Keystone Plumbing</span>
  </section>
</main>
</body>
</html>
```